Business Card & Stationary Design Project

We are looking for some creative direction for business cards and our stationary.

We are a global logistics firm that has recently changed its name to Marwick Global Logistics and we have a new website due out tomorrow (www.marwick.com.au).

The colours of the company are rich navy tones, I would like to have business cards that fit together to make one picture on the back (possibly an old map of the world??), and the front to be modern contemporary looking.

But I am open to suggestions, so just incorporate our new logo and get going!
Updates

Hi Everyone,

Thank you for all of your designs so far and the time you have put into it.

I have asked many of you for amendments to see if we can get a final product, so with this in mind I am extending the deadline by a few days.

Good luck and thank you once again.

Please message me direct if you need any clarification.

Kind Regards
Tobias

Reason: As outlined the extra 3 days is for amendments and changes to the current submissions. Thanks Tobias

Industry/Entity Type

Business

```html
<!DOCTYPE html>
<html lang="en">
<head>
<meta charset="utf-8">
<title>Marwick Global Logistics – Business Card</title>
<link rel="stylesheet" href="https://fonts.googleapis.com/css2?family=Cinzel:wght@500&family=Crimson+Pro:wght@400&family=Open+Sans:wght@400&display=swap">
<style>
  :root {
    --page-bg: #e6e9ee;
    --navy-light: #2d4f88;
    --navy-dark: #1c3766;
    --sky-light: #a7d3f1;
    --sky-dark: #76a9cf;
    --ink-navy: #1f3a6b;
    --ink-text: #2a3e62;
    --white: #ffffff;
    --globe-light: #5f8fd0;
    --globe-mid: #2c5aa3;
    --globe-dark: #173b78;
  }
  * { margin: 0; padding: 0; box-sizing: border-box; }
  html, body {
    width: 1200px;
    height: 1100px;
    overflow: hidden;
    background: var(--page-bg);
  }
  .sheet {
    position: relative;
    width: 1200px;
    height: 1100px;
  }
  .card {
    position: absolute;
    left: 161px;
    width: 878px;
    height: 507px;
    border-radius: 28px;
    overflow: hidden;
  }
  .card--front {
    top: 28px;
    background: radial-gradient(ellipse at 40% 55%, var(--navy-light) 0%, var(--navy-dark) 85%);
  }
  .card--back {
    top: 565px;
    background: radial-gradient(ellipse at 50% 40%, var(--sky-light) 0%, var(--sky-dark) 90%);
  }
  .wordmark {
    position: absolute;
    font-family: "Cinzel", serif;
    font-weight: 500;
    line-height: 1;
  }
  .wordmark__name {
    display: block;
    font-size: 42px;
    letter-spacing: 10px;
  }
  .wordmark__tagline {
    display: block;
    margin-top: 4px;
    font-size: 15px;
    letter-spacing: 6.2px;
  }
  .card--front .wordmark {
    left: 72px;
    top: 232px;
    color: var(--white);
  }
  .card--back .wordmark {
    left: 46px;
    top: 234px;
    color: var(--ink-navy);
  }
  .globe {
    position: absolute;
    left: 420px;
    top: 32px;
    width: 412px;
    height: 412px;
    border-radius: 50%;
    background: radial-gradient(circle at 38% 32%, var(--globe-light) 0%, var(--globe-mid) 50%, var(--globe-dark) 100%);
    box-shadow: 0 0 0 2px rgba(255,255,255,0.15), 0 12px 30px rgba(0,0,0,0.35);
  }
  .divider {
    position: absolute;
    left: 409px;
    top: 176px;
    width: 1px;
    height: 178px;
    background: var(--ink-navy);
    opacity: 0.7;
  }
  .holder-name {
    position: absolute;
    left: 436px;
    top: 212px;
    font-family: "Crimson Pro", serif;
    font-size: 37px;
    color: var(--ink-navy);
  }
  .contact {
    position: absolute;
    left: 467px;
    top: 264px;
    font-family: "Open Sans", sans-serif;
    font-size: 15.5px;
    color: var(--ink-text);
    list-style: none;
  }
  .contact li { height: 27px; white-space: nowrap; }
  .contact__label {
    display: inline-block;
    font-family: "Crimson Pro", serif;
    font-size: 17px;
    margin-right: 8px;
  }
  .contact li:not(:first-child) .contact__label { width: 72px; margin-left: 4px; margin-right: 0; }
</style>
</head>
<body>
<main class="sheet">
  <section class="card card--front">
    <div class="wordmark">
      <span class="wordmark__name">MARWICK</span>
      <span class="wordmark__tagline">GLOBAL LOGISTICS</span>
    </div>
    <div class="globe" role="img" aria-label="Glossy blue globe showing Asia and Australia"></div>
  </section>

  <section class="card card--back">
    <div class="wordmark">
      <span class="wordmark__name">MARWICK</span>
      <span class="wordmark__tagline">GLOBAL LOGISTICS</span>
    </div>
    <div class="divider"></div>
    <h1 class="holder-name">Your Full Name</h1>
    <ul class="contact">
      <li><span class="contact__label">your adress,</span>58 Harbour Row</li>
      <li><span class="contact__label">Phone :</span>02 7410 2265</li>
      <li><span class="contact__label">Email :</span>info@marwick.com.au</li>
    </ul>
  </section>
</main>
</body>
</html>
```